new business card and logo for a high end Automotive repair and performance shop

Need to update our design for our business cards. New address, and want a new look. I'll upload some pics of our current card. We are a high end auto repair/tuning shop. New address will be 5192 W. Larkfield Ave Brookhaven, T.X. 70418. I do have the vector files if needed. The logo would have a similar design. Love the look of carbon fiber, and brushed aluminum, although may have issues showing the texture of the material due to dpi restrictions during card printing. Also the logo would have to be easily printed on shirts, and for embroidery. Thanks, and good luck.

www.motor-zenith.example

Target Market(s)

High end automotive repair, dealership alternative.

Industry/Entity Type

Automotive

Contact Information for Business Card

MOTORZENITH
5192 W. LARKFIELD AVE
BROOKHAVEN, T.X. 70418
PH 555-307-9261
FAX 555-307-4470
EMAIL INFO@MOTOR-ZENITH.EXAMPLE

Logo Text

MotorZenith

Font styles to use
Sans Serif

Requirements
Must have
• name, address, description that was uploaded.
Nice to have
• maybe some brands i.e. vardo, orvex, Talvani, qrt, solvanta, dovik etc. not necessary. simple is good, like the look of carbon fiber, brushed aluminum.
Should not have
• open to all suggestions.

```html
<!DOCTYPE html>
<html lang="en">
<head>
<meta charset="utf-8">
<title>MotorZenith Business Card</title>
<link rel="stylesheet" href="https://fonts.googleapis.com/css2?family=Open+Sans:wght@300;400;600;700&display=swap">
<style>
  :root {
    --canvas: #e6e6e6;
    --carbon: #2a2a2c;
    --carbon-light: #333336;
    --name-band: #38383b;
    --accent: #e63e44;
    --white: #ffffff;
    --ink: #1b1b1b;
    --text-light: #e8e8e8;
    --silver: #b9b9bc;
  }
  * { box-sizing: border-box; margin: 0; padding: 0; }
  html, body { width: 1200px; height: 1000px; overflow: hidden; }
  body {
    background: var(--canvas);
    font-family: "Open Sans", Arial, sans-serif;
    position: relative;
  }
  .card {
    position: absolute;
    left: 290px;
    width: 620px;
    height: 354px;
    overflow: hidden;
    box-shadow: 0 10px 24px rgba(0,0,0,0.18);
  }
  .card--front { top: 100px; display: flex; }
  .card--back { top: 546px; background: linear-gradient(135deg, var(--carbon-light), var(--carbon)); }

  /* front */
  .front__brand {
    width: 250px; height: 100%;
    background: var(--white);
    display: flex; align-items: center; justify-content: center; gap: 10px;
  }
  .brand-mark { width: 14px; height: 14px; border-radius: 50%; background: var(--accent); flex: none; }
  .brand-name { font-weight: 700; font-size: 24px; color: var(--ink); letter-spacing: 0.5px; }
  .front__info {
    flex: 1; height: 100%;
    background: linear-gradient(135deg, var(--carbon-light), var(--carbon));
    display: flex; flex-direction: column;
  }
  .name-band {
    background: var(--name-band);
    display: flex; align-items: center; gap: 16px;
    padding: 22px 30px;
  }
  .person-name { color: var(--white); font-size: 26px; font-weight: 300; letter-spacing: 0.5px; line-height: 1.1; }
  .person-name strong { font-weight: 700; }
  .person-role { color: var(--accent); font-size: 13px; letter-spacing: 1.5px; text-transform: uppercase; }
  .contacts { list-style: none; padding: 24px 30px; display: flex; flex-direction: column; gap: 16px; position: relative; }
  .contacts::before {
    content: ""; position: absolute; left: 46px; top: 40px; bottom: 40px;
    border-left: 1px dashed var(--accent);
  }
  .contact { display: flex; align-items: center; gap: 16px; color: var(--text-light); font-size: 14px; line-height: 1.45; position: relative; }
  .hex { width: 32px; height: 34px; flex: none; }

  /* back */
  .back__band {
    position: absolute; left: 70px; top: 0; width: 56px; height: 100%;
    background: var(--accent);
    display: flex; align-items: center; justify-content: center;
  }
  .back__url {
    color: var(--white); font-size: 13px; letter-spacing: 0.5px;
    transform: rotate(-90deg); white-space: nowrap;
  }
  .back__rule { position: absolute; right: 70px; top: 0; width: 1px; height: 100%; background: var(--accent); }
  .back__brand {
    position: absolute; left: 126px; right: 71px; top: 0; bottom: 0;
    display: flex; align-items: center; justify-content: center; gap: 12px;
  }
  .back__brand .brand-name { color: var(--silver); font-size: 30px; }
  .back__brand .brand-mark { background: var(--silver); width: 16px; height: 16px; }
</style>
</head>
<body>

<section class="card card--front" aria-label="Business card front">
  <div class="front__brand">
    <span class="brand-mark"></span>
    <span class="brand-name">MotorZenith</span>
  </div>
  <div class="front__info">
    <div class="name-band">
      <svg class="hex" viewBox="0 0 32 34" aria-hidden="true">
        <polygon points="16,2 29,9.5 29,24.5 16,32 3,24.5 3,9.5" fill="var(--accent)"/>
        <circle cx="16" cy="13" r="4" fill="var(--white)"/>
        <path d="M9.5 25 Q16 15 22.5 25 Z" fill="var(--white)"/>
      </svg>
      <div>
        <p class="person-name"><strong>DALE</strong> HARTWELL</p>
        <p class="person-role">Owner</p>
      </div>
    </div>
    <ul class="contacts">
      <li class="contact">
        <svg class="hex" viewBox="0 0 32 34" aria-hidden="true">
          <polygon points="16,2 29,9.5 29,24.5 16,32 3,24.5 3,9.5" fill="var(--carbon)" stroke="var(--accent)" stroke-width="2"/>
          <path d="M11 11 h4 l1 4 -2 1.5 q1.5 3 4 4.5 l1.5 -2 4 1 v4 q-10 0 -12.5 -13z" fill="var(--white)"/>
        </svg>
        <span>555-307-9261<br>555-307-4470</span>
      </li>
      <li class="contact">
        <svg class="hex" viewBox="0 0 32 34" aria-hidden="true">
          <polygon points="16,2 29,9.5 29,24.5 16,32 3,24.5 3,9.5" fill="var(--carbon)" stroke="var(--accent)" stroke-width="2"/>
          <circle cx="16" cy="17" r="6.5" fill="none" stroke="var(--white)" stroke-width="1.5"/>
          <ellipse cx="16" cy="17" rx="2.8" ry="6.5" fill="none" stroke="var(--white)" stroke-width="1.2"/>
          <line x1="9.5" y1="17" x2="22.5" y2="17" stroke="var(--white)" stroke-width="1.2"/>
        </svg>
        <span>info@motor-zenith.example<br>www.motor-zenith.example</span>
      </li>
      <li class="contact">
        <svg class="hex" viewBox="0 0 32 34" aria-hidden="true">
          <polygon points="16,2 29,9.5 29,24.5 16,32 3,24.5 3,9.5" fill="var(--carbon)" stroke="var(--accent)" stroke-width="2"/>
          <path d="M16 25 q-6 -7 -6 -11 a6 6 0 0 1 12 0 q0 4 -6 11z" fill="var(--white)"/>
          <circle cx="16" cy="14" r="2.2" fill="var(--carbon)"/>
        </svg>
        <span>5192 W. Larkfield Ave Brookhaven,<br>T.X 70418</span>
      </li>
    </ul>
  </div>
</section>

<section class="card card--back" aria-label="Business card back">
  <div class="back__band"><span class="back__url">www.motor-zenith.example</span></div>
  <div class="back__rule"></div>
  <div class="back__brand">
    <span class="brand-mark"></span>
    <span class="brand-name">MotorZenith</span>
  </div>
</section>

</body>
</html>
```